Creative Stationary For Security Solutions Company
Halvern Guard Services
Creative Stationary For Security Solutions Company - Security
Creative Brief
Professional
Wesley Kolvasky
wesley@halvernguard.example
www.halvernguard.example
California PI No. 51928 And California PPO No. 40261
Logo has been uploaded in different color variations. Feel free to experiment, however I prefer the logo with black highlights on the visor, nose and neck (#1 I believe) I will provide my phone numbers towards the end of the project. Thanks and have fun.
I would like to see my logo on one side and info on the other. But feel free to experiment.

```html
<!DOCTYPE html>
<html lang="en">
<head>
<meta charset="utf-8">
<title>Halvern Guard Services — Stationery Set</title>
<link href="https://fonts.googleapis.com/css2?family=Montserrat:wght@400;600;700;800&family=Open+Sans:wght@400;600&display=swap" rel="stylesheet">
<style>
  :root {
    --orange: #f26b1d;
    --black: #1b1b1b;
    --ink: #3a3a3a;
    --grey: #8a8a8a;
    --paper: #ffffff;
    --stage: #ffffff;
    --shadow: 0 2px 8px rgba(0,0,0,0.18);
  }
  * { margin: 0; padding: 0; box-sizing: border-box; }
  html, body { width: 1200px; height: 936px; overflow: hidden; background: var(--stage); }
  body { position: relative; font-family: "Open Sans", Arial, sans-serif; color: var(--ink); }

  .sheet { position: absolute; background: var(--paper); box-shadow: var(--shadow); overflow: hidden; }
  .sheet .edge { position: absolute; top: 0; height: 100%; }

  .brand { position: absolute; display: flex; align-items: center; gap: 6px; }
  .brand-dot { border-radius: 50%; background: var(--orange); flex: none; }
  .brand-name { font-family: "Montserrat", Arial, sans-serif; font-weight: 800; color: var(--black); line-height: 1.05; text-transform: uppercase; }
  .brand-name span { display: block; }

  /* Letterhead */
  .letterhead { left: 178px; top: 46px; width: 400px; height: 576px; }
  .letterhead .brand { left: 18px; top: 22px; }
  .letterhead .brand-dot { width: 22px; height: 22px; }
  .letterhead .brand-name { font-size: 12px; }
  .letterhead .brand-name span + span { font-size: 6px; letter-spacing: 0.6px; }
  .letter-body { position: absolute; left: 24px; top: 96px; width: 288px; font-size: 5.2px; line-height: 1.55; color: var(--ink); }
  .letter-body p { margin-bottom: 7px; }
  .letter-body .recipient { margin-bottom: 10px; }
  .letter-body .signoff { margin-top: 12px; }
  .letter-body .signature-space { height: 16px; }
  .letter-body .sender { font-weight: 600; color: var(--black); }
  .letter-contacts { position: absolute; left: 24px; bottom: 30px; font-size: 5px; line-height: 1.9; list-style: none; }
  .letter-contacts li { display: flex; align-items: center; gap: 4px; }
  .contact-icon { width: 6px; height: 6px; border-radius: 50%; background: var(--orange); flex: none; }

  /* Folder */
  .folder { left: 634px; top: 25px; width: 498px; height: 609px; }
  .folder .brand { left: 258px; top: 392px; flex-direction: column; align-items: flex-start; gap: 10px; }
  .folder .brand-dot { width: 66px; height: 66px; }
  .folder .brand-name { font-size: 38px; }
  .folder .brand-name span + span { font-size: 13.5px; letter-spacing: 1.6px; margin-top: 4px; }

  /* Business cards */
  .card-front { left: 51px; top: 655px; width: 172px; height: 86px; }
  .card-front .brand { left: 16px; top: 16px; flex-direction: column; align-items: flex-start; gap: 4px; }
  .card-front .brand-dot { width: 16px; height: 16px; }
  .card-front .brand-name { font-size: 8px; }
  .card-front .brand-name span + span { font-size: 3.6px; letter-spacing: 0.3px; }
  .card-details { position: absolute; left: 86px; top: 14px; font-size: 4px; line-height: 1.7; }
  .card-details .person { font-family: "Montserrat", Arial, sans-serif; font-weight: 700; font-size: 6px; color: var(--orange); }
  .card-details .role { color: var(--grey); margin-bottom: 4px; }
  .card-details ul { list-style: none; }
  .card-details li { display: flex; align-items: center; gap: 3px; }
  .card-details .contact-icon { width: 4px; height: 4px; }

  .card-back { left: 51px; top: 776px; width: 172px; height: 102px; background: var(--black); }
  .card-back .brand { left: 50%; top: 50%; transform: translate(-50%, -50%); flex-direction: column; gap: 5px; }
  .card-back .brand-dot { width: 20px; height: 20px; }
  .card-back .brand-name { font-size: 11px; color: #ffffff; text-align: center; }
  .card-back .brand-name span + span { font-size: 4.8px; letter-spacing: 0.5px; }

  /* Envelopes */
  .envelope-front { left: 261px; top: 665px; width: 437px; height: 213px; }
  .envelope-front .brand { left: 22px; top: 20px; }
  .envelope-front .brand-dot { width: 18px; height: 18px; }
  .envelope-front .brand-name { font-size: 10px; }
  .envelope-front .brand-name span + span { font-size: 5px; letter-spacing: 0.5px; }

  .envelope-back { left: 731px; top: 665px; width: 436px; height: 210px; }
  .envelope-back .brand { left: 50%; top: 24px; transform: translateX(-50%); }
  .envelope-back .brand-dot { width: 14px; height: 14px; }
  .envelope-back .brand-name { font-size: 7px; color: var(--orange); }
</style>
</head>
<body>

  <!-- Letterhead -->
  <section class="sheet letterhead" aria-label="Letterhead">
    <svg class="edge" style="left:0;width:400px" viewBox="0 0 400 576" aria-hidden="true">
      <path d="M336 0 Q312 288 336 576 L350 576 Q326 288 350 0 Z" fill="var(--orange)"/>
      <path d="M352 0 Q328 288 352 576 L400 576 L400 0 Z" fill="var(--black)"/>
    </svg>
    <div class="brand">
      <div class="brand-dot"></div>
      <div class="brand-name"><span>Halvern</span><span>Guard Services</span></div>
    </div>
    <div class="letter-body">
      <p>June 14, 2024</p>
      <p class="recipient">Dear Client,<br>120 Harbor Lane, Suite 4, Fresno CA</p>
      <p>Thank you for choosing our team to protect your property and people. Our licensed officers provide patrol, event and site security across the state, with clear reporting and quick response times. We review every assignment with you before work begins so that expectations, schedules and access points are fully understood by all staff on duty.</p>
      <p>Our private investigation division supports legal, insurance and corporate clients with discreet research, surveillance and background checks. Every case is handled by trained staff and documented in plain reports you can rely on. Please contact our office with any questions about this proposal or to arrange a site visit at a time that suits you.</p>
      <p>We look forward to working with you and keeping your business safe throughout the coming year.</p>
      <p class="signoff">Best Regards,</p>
      <div class="signature-space"></div>
      <p><span class="sender">Wesley Kolvasky</span><br>Chief Executive Officer</p>
    </div>
    <ul class="letter-contacts">
      <li><span class="contact-icon"></span>+1 (555) 014-8820</li>
      <li><span class="contact-icon"></span>+1 (555) 014-8821</li>
      <li><span class="contact-icon"></span>wesley@halvernguard.example</li>
      <li><span class="contact-icon"></span>www.halvernguard.example</li>
    </ul>
  </section>

  <!-- Presentation folder -->
  <section class="sheet folder" aria-label="Presentation folder">
    <svg class="edge" style="left:0;width:498px" viewBox="0 0 498 609" aria-hidden="true">
      <path d="M0 0 L62 0 Q10 305 62 609 L0 609 Z" fill="var(--black)"/>
      <path d="M64 0 Q12 305 64 609 L82 609 Q30 305 82 0 Z" fill="var(--orange)"/>
    </svg>
    <div class="brand">
      <div class="brand-dot"></div>
      <div class="brand-name"><span>Halvern</span><span>Guard Services</span></div>
    </div>
  </section>

  <!-- Business card, front -->
  <section class="sheet card-front" aria-label="Business card front">
    <svg class="edge" style="left:0;width:172px" viewBox="0 0 172 86" aria-hidden="true">
      <path d="M0 0 L6 0 Q0 43 6 86 L0 86 Z" fill="var(--black)"/>
      <path d="M7 0 Q1 43 7 86 L10 86 Q4 43 10 0 Z" fill="var(--orange)"/>
    </svg>
    <div class="brand">
      <div class="brand-dot"></div>
      <div class="brand-name"><span>Halvern</span><span>Guard Services</span></div>
    </div>
    <div class="card-details">
      <div class="person">Wesley Kolvasky</div>
      <div class="role">Chief Executive Officer</div>
      <ul>
        <li><span class="contact-icon"></span>+1 (555) 014-8820</li>
        <li><span class="contact-icon"></span>wesley@halvernguard.example</li>
        <li><span class="contact-icon"></span>www.halvernguard.example</li>
      </ul>
    </div>
  </section>

  <!-- Business card, back -->
  <section class="sheet card-back" aria-label="Business card back">
    <svg class="edge" style="left:0;width:172px" viewBox="0 0 172 102" aria-hidden="true">
      <path d="M0 0 L8 0 Q0 51 8 102 L0 102 Z" fill="var(--orange)"/>
    </svg>
    <div class="brand">
      <div class="brand-dot"></div>
      <div class="brand-name"><span>Halvern</span><span>Guard Services</span></div>
    </div>
  </section>

  <!-- Envelope, front -->
  <section class="sheet envelope-front" aria-label="Envelope front">
    <svg class="edge" style="left:0;width:437px" viewBox="0 0 437 213" aria-hidden="true">
      <path d="M378 0 Q364 106 378 213 L386 213 Q372 106 386 0 Z" fill="var(--orange)"/>
      <path d="M388 0 Q374 106 388 213 L437 213 L437 0 Z" fill="var(--black)"/>
    </svg>
    <div class="brand">
      <div class="brand-dot"></div>
      <div class="brand-name"><span>Halvern</span><span>Guard Services</span></div>
    </div>
  </section>

  <!-- Envelope, back -->
  <section class="sheet envelope-back" aria-label="Envelope back">
    <svg class="edge" style="left:0;width:436px" viewBox="0 0 436 210" aria-hidden="true">
      <path d="M0 0 L436 0 L436 58 Q330 66 260 86 L218 100 L176 86 Q106 66 0 58 Z" fill="var(--black)"/>
      <path d="M0 58 Q106 66 176 86 L218 100 L260 86 Q330 66 436 58 L436 62 Q330 70 260 90 L218 104 L176 90 Q106 70 0 62 Z" fill="var(--orange)"/>
      <rect x="150" y="14" width="136" height="30" rx="3" fill="#ffffff"/>
    </svg>
    <div class="brand">
      <div class="brand-dot"></div>
      <div class="brand-name">Halvern</div>
    </div>
  </section>

</body>
</html>
```